banner ad for a very high end interior designer

Our website only gets a small number of hits per day, but it is often people looking to choose designers to interview. We are going to do a Zolvex remarketing campaign to show ads to people who have previously visited our website. The goal is to make sure they remember the quality and sophistication of our work.
The banner should include pictures of our work. You can see this at www.corinnebalastrodesign.com. Perhaps a single image per banner, or a slideshow within the banner?
The goal is to create awareness and to remind the former website visitor of our work. So it is important to include the logo from our website in the banner ad for visual anchoring and recall. As well, the banner graphics should be of a quality that would be used by Osric Tambel or Pavo Lenk or wexley cousins or vorna or Castelmo.
As for a 'call to action', we can offer "See Our Work in Person" or some simpler wording. If the person clicks on the banner, it will take them to a landing page where they can request free tickets to the Larkmont Residence Interiors Pavilion home. We are designing one of the rooms at that open home event.
Size: either 300 x 250. May buy a second at 320 x 100

```html
<!DOCTYPE html>
<html lang="en">
<head>
<meta charset="utf-8">
<title>Corinne Balastro – Banner Ads</title>
<link rel="stylesheet" href="https://fonts.googleapis.com/css2?family=Fjalla+One&family=Open+Sans:wght@400;600&family=Roboto+Condensed:wght@700&family=Tinos&display=swap">
<style>
  :root {
    --stage-dark: #2f140f;
    --stage-light: #ffffff;
    --ink-brown: #2e150c;
    --ink-black: #111111;
    --gold: #f2b51f;
    --orange: #f0a030;
    --logo-grey: #6b6b6b;
    --paper: rgba(255,255,255,0.82);
    --frame: #a89c96;
  }
  * { margin: 0; padding: 0; box-sizing: border-box; }
  html, body { width: 1200px; height: 1000px; overflow: hidden; }
  body { position: relative; background: var(--stage-light); font-family: 'Open Sans', sans-serif; }

  .stage-top { position: absolute; left: 0; top: 0; width: 1200px; height: 540px; background: var(--stage-dark); }

  /* 300 x 250 rectangle */
  .ad-rect { position: absolute; width: 300px; height: 250px; overflow: hidden; }
  .ad-rect .photo {
    position: absolute; inset: 0;
    background:
      radial-gradient(ellipse 60px 50px at 150px 60px, #d9a53a 0%, rgba(217,165,58,0) 100%),
      linear-gradient(180deg, #c9bba9 0%, #e9e1d4 18%, #bfa58a 45%, #8a5a3a 68%, #4a2c1c 85%, #2a170d 100%);
  }
  .ad-rect .logo-band { position: absolute; left: 0; top: 14px; width: 300px; height: 42px; background: var(--paper); }
  .ad-rect .logo { position: absolute; left: 0; top: 28px; width: 300px; display: flex; justify-content: center; align-items: center; gap: 6px; }
  .ad-rect .logo-mark { width: 7px; height: 7px; background: var(--gold); }
  .ad-rect .logo-name { font-size: 11px; letter-spacing: 1.6px; color: var(--logo-grey); }
  .ad-rect .headline { position: absolute; left: 0; top: 66px; width: 300px; text-align: center; font-family: 'Fjalla One', sans-serif; font-size: 37px; line-height: 44px; color: var(--ink-brown); text-shadow: 0 0 8px rgba(255,255,255,0.8); }
  .ad-rect .subhead { position: absolute; left: 0; top: 108px; width: 300px; text-align: center; font-family: 'Tinos', serif; font-size: 22px; color: #000; }
  .ad-rect .phone { position: absolute; left: 0; top: 170px; width: 300px; text-align: center; font-family: 'Roboto Condensed', sans-serif; font-weight: 700; font-size: 27px; color: #fff; }
  .ad-rect .rule { position: absolute; left: 62px; width: 176px; height: 1px; background: rgba(255,255,255,0.6); }
  .ad-rect .email { position: absolute; left: 0; top: 208px; width: 300px; text-align: center; font-size: 11px; font-weight: 600; letter-spacing: 1.2px; color: #fff; }
  .ad-rect .url-band { position: absolute; left: 0; top: 228px; width: 300px; height: 22px; background: rgba(20,10,5,0.85); }
  .ad-rect .url { position: absolute; left: 0; top: 231px; width: 300px; text-align: center; font-size: 11px; font-weight: 600; letter-spacing: 1px; color: var(--gold); }

  /* 320 x 100 mobile banner */
  .ad-strip { position: absolute; width: 320px; height: 100px; overflow: hidden; }
  .ad-strip .photo {
    position: absolute; inset: 0;
    background: linear-gradient(90deg, #f4f3f1 0%, #ecebe8 35%, #d9d6d0 55%, #c9c3b8 70%, #e6e3de 100%);
  }
  .ad-strip .photo-lower { position: absolute; left: 0; top: 64px; width: 320px; height: 36px; background: linear-gradient(90deg, #e9e9ea, #cfd0d3 50%, #e2e2e2); }
  .ad-strip .headline { position: absolute; left: 7px; top: 6px; font-family: 'Fjalla One', sans-serif; font-size: 20px; line-height: 24px; color: var(--orange); }
  .ad-strip .subhead { position: absolute; left: 7px; top: 28px; font-size: 12px; color: var(--ink-black); }
  .ad-strip .phone { position: absolute; left: 7px; top: 45px; font-family: 'Roboto Condensed', sans-serif; font-weight: 700; font-size: 19px; letter-spacing: 1px; color: var(--ink-black); }
  .ad-strip .email { position: absolute; left: 8px; top: 69px; font-size: 9px; color: var(--ink-black); }
  .ad-strip .url { position: absolute; left: 8px; top: 82px; font-size: 9px; color: var(--ink-black); }
  .ad-strip .logo-box { position: absolute; left: 212px; top: 66px; width: 108px; height: 30px; background: rgba(255,255,255,0.92); }
  .ad-strip .logo { position: absolute; left: 212px; top: 75px; width: 108px; display: flex; justify-content: center; align-items: center; gap: 4px; }
  .ad-strip .logo-mark { width: 5px; height: 5px; background: var(--gold); }
  .ad-strip .logo-name { font-size: 7.5px; letter-spacing: 1px; color: var(--logo-grey); }

  .framed { outline: 1px solid var(--frame); }
</style>
</head>
<body>
  <div class="stage-top"></div>

  <!-- dark presentation -->
  <div class="ad-rect" style="left:220px; top:170px;">
    <div class="photo" role="img" aria-label="Photo of a refined dining room with leather armchairs, round table and shuttered windows"></div>
    <div class="logo-band"></div>
    <div class="logo"><span class="logo-mark"></span><span class="logo-name">CORINNE BALASTRO</span></div>
    <div class="headline">High-End</div>
    <div class="subhead">Residential Interiors</div>
    <div class="phone">415-555-0142</div>
    <div class="rule" style="top:203px;"></div>
    <div class="email">info@CorinneBalastro.com</div>
    <div class="url-band"></div>
    <div class="url">www.corinnebalastrodesign.com</div>
  </div>

  <div class="ad-strip" style="left:567px; top:170px;">
    <div class="photo" role="img" aria-label="Photo of a bright living room with gilt mirror, lamp and pale sofa"></div>
    <div class="photo-lower"></div>
    <div class="headline">HIGH-END</div>
    <div class="subhead">Residential Interiors</div>
    <div class="phone">415-555-0142</div>
    <div class="email">info@CorinneBalastro.com</div>
    <div class="url">www.corinnebalastrodesign.com</div>
    <div class="logo-box"></div>
    <div class="logo"><span class="logo-mark"></span><span class="logo-name">CORINNE BALASTRO</span></div>
  </div>

  <!-- light presentation -->
  <div class="ad-rect framed" style="left:234px; top:620px;">
    <div class="photo" role="img" aria-label="Photo of a refined dining room with leather armchairs, round table and shuttered windows"></div>
    <div class="logo-band"></div>
    <div class="logo"><span class="logo-mark"></span><span class="logo-name">CORINNE BALASTRO</span></div>
    <div class="headline">High-End</div>
    <div class="subhead">Residential Interiors</div>
    <div class="phone">415-555-0142</div>
    <div class="rule" style="top:203px;"></div>
    <div class="email">info@CorinneBalastro.com</div>
    <div class="url-band"></div>
    <div class="url">www.corinnebalastrodesign.com</div>
  </div>

  <div class="ad-strip framed" style="left:581px; top:620px;">
    <div class="photo" role="img" aria-label="Photo of a bright living room with gilt mirror, lamp and pale sofa"></div>
    <div class="photo-lower"></div>
    <div class="headline">HIGH-END</div>
    <div class="subhead">Residential Interiors</div>
    <div class="phone">415-555-0142</div>
    <div class="email">info@CorinneBalastro.com</div>
    <div class="url">www.corinnebalastrodesign.com</div>
    <div class="logo-box"></div>
    <div class="logo"><span class="logo-mark"></span><span class="logo-name">CORINNE BALASTRO</span></div>
  </div>
</body>
</html>
```